Design uplift of Quillamber.com site

The site needs to be fast and responsive down to mobile.
Needs to use the supplied Video as the homepage background.
Needs to use Generate Press as the theme - Site theme to be a child theme of Generate Press.
Needs to have a button above the fold for an offer of a free email course on how to set up a medical software project.
Needs to use the Quillamber logo. This logo has been trademarked.

The existing site is at: www.quillamber.com

```html
<!DOCTYPE html>
<html lang="en">
<head>
<meta charset="utf-8">
<title>Quillamber – Medical Software Development</title>
<link href="https://fonts.googleapis.com/css2?family=Poppins:wght@400;500;600;700&display=swap" rel="stylesheet">
<style>
:root{
  --blue:#139fe0;
  --blue-dark:#0b7fc0;
  --ink:#1d2733;
  --text:#3b4450;
  --muted:#6b7480;
  --soft:#f4f5f7;
  --blog-bg:#eef7fb;
  --footer:#0e1013;
  --white:#ffffff;
}
*{box-sizing:border-box;margin:0;padding:0}
html,body{width:1200px;height:3617px;overflow:hidden}
body{font-family:'Poppins',sans-serif;color:var(--text);background:var(--white);position:relative}
section,header,footer{position:absolute;left:0;width:1200px}
.abs{position:absolute}
.btn{position:absolute;display:flex;align-items:center;justify-content:center;gap:5px;background:var(--blue);color:var(--white);border-radius:20px;font-weight:600;font-size:13px;text-transform:uppercase;letter-spacing:.2px}
.btn .dot{width:11px;height:11px;border-radius:50%;background:var(--white);display:inline-flex;align-items:center;justify-content:center}
.btn .dot::after{content:"";border-left:4px solid var(--blue);border-top:3px solid transparent;border-bottom:3px solid transparent;margin-left:1px}

/* hero */
.hero{top:0;height:706px;background:linear-gradient(120deg,#0b1a33 0%,#1d3c68 40%,#2f5d8e 65%,#132a4b 100%)}
.brand{position:absolute;display:flex;align-items:center;gap:10px;color:var(--white);font-weight:600;font-size:28px}
.brand .mark{width:44px;height:44px;border-radius:50%;border:3px solid var(--white)}
.nav{position:absolute;top:32px;left:390px;display:flex;gap:0;font-size:14px;font-weight:500;color:var(--white)}
.nav a{position:absolute;white-space:nowrap;color:var(--white);text-decoration:none}
.nav a.active{color:var(--blue);border-bottom:2px solid var(--blue);padding-bottom:4px}
.btn-outline{background:transparent;border:2px solid var(--blue);color:var(--blue)}
.btn-outline .dot{background:var(--blue)}
.btn-outline .dot::after{border-left-color:var(--white)}
.hero-title{left:102px;top:358px;font-size:39px;font-weight:600;line-height:43px;color:var(--white)}

/* welcome */
.welcome{top:706px;height:606px;background:var(--white)}
.welcome .panel{left:46px;top:80px;width:249px;height:300px;background:#e8f4fb;border-radius:14px}
.welcome .photo{left:100px;top:123px;width:470px;height:381px;border-radius:6px;background:linear-gradient(135deg,#c9ced4,#8f99a4 50%,#5b6470)}
.welcome .dots{left:46px;top:345px;width:190px;height:190px;background-image:radial-gradient(#bcdff2 1.5px,transparent 1.6px);background-size:10px 10px}
.welcome .eyebrow{left:623px;top:178px;border-left:4px solid var(--blue);padding-left:10px}
.eyebrow .small{color:var(--blue);font-size:26px;font-weight:600;line-height:30px}
.eyebrow .big{color:var(--ink);font-size:53px;font-weight:600;line-height:54px}
.welcome p{left:623px;top:270px;width:466px;font-size:14.5px;line-height:30px;text-align:justify}

/* services */
.services{top:1312px;height:482px;background:var(--soft)}
.section-title{position:absolute;left:0;width:1200px;text-align:center;color:var(--ink);font-size:45px;font-weight:600}
.card{position:absolute;top:148px;width:235px;height:238px;background:var(--white);border-radius:8px;box-shadow:0 2px 10px rgba(0,0,0,.06);text-align:center}
.card svg{margin-top:30px}
.card h3{margin-top:14px;font-size:23px;font-weight:600;line-height:30px;color:var(--ink)}

/* feature band */
.feature{top:1794px;height:561px;background:linear-gradient(90deg,#1592d6 0%,#3aa7e0 40%,#a7cde4 65%,#dce8ef 100%)}
.feature h2{left:96px;top:110px;font-size:45px;line-height:44px;font-weight:600;color:var(--white)}
.feature p{left:104px;top:227px;width:442px;font-size:15px;line-height:30px;color:var(--white);text-align:justify}

/* blog */
.blog{top:2355px;height:750px;background:var(--blog-bg)}
.post{position:absolute;background:var(--white);border-radius:6px;overflow:hidden;box-shadow:0 2px 10px rgba(0,0,0,.05)}
.post .meta{font-size:11.5px;color:var(--blue)}
.post h3{color:var(--ink);font-weight:600;font-size:21px;line-height:27px}
.post p{font-size:13px;line-height:23px;color:var(--text)}
.post .more{color:var(--blue);font-size:14px;font-weight:600;display:flex;align-items:center;gap:5px}
.more .dot{width:12px;height:12px;border-radius:50%;background:var(--blue);display:inline-flex;align-items:center;justify-content:center}
.more .dot::after{content:"";border-left:4px solid var(--white);border-top:3px solid transparent;border-bottom:3px solid transparent;margin-left:1px}
.to-top{left:1125px;top:535px;width:50px;height:50px;border-radius:50%;background:var(--white);box-shadow:0 2px 8px rgba(0,0,0,.08)}

/* newsletter */
.signup{top:3105px;height:123px;background:var(--blue);color:var(--white)}
.signup h2{left:98px;top:30px;font-size:29px;font-weight:600}
.signup .sub{left:100px;top:72px;font-size:12px}
.signup .field{left:556px;top:39px;width:530px;height:46px;background:var(--white);border-radius:3px;font-size:12px;color:#444;padding:14px 14px}
.signup .submit{left:949px;top:42px;width:134px;height:40px;background:var(--blue);color:var(--white);font-weight:600;font-size:15px;display:flex;align-items:center;justify-content:center;border-radius:2px}

/* footer */
.footer{top:3228px;height:389px;background:var(--footer);color:var(--white)}
.footer h4{position:absolute;top:88px;font-size:19px;font-weight:600;text-decoration:underline;text-underline-offset:5px}
.footer .list{position:absolute;top:134px;font-size:16px;line-height:33.5px}
.footer .about{left:100px;top:178px;width:290px;font-size:13px;line-height:23px}
.contact-row{position:absolute;left:630px;display:flex;gap:12px;font-size:16px;line-height:25px}
.social{position:absolute;top:128px;width:34px;height:34px;border-radius:50%;border:1.5px solid var(--white)}
.footer .rule{left:100px;top:326px;width:1000px;height:1px;background:#2a2d33}
.footer .legal{top:348px;font-size:13px}
</style>
</head>
<body>

<header class="hero">
  <div class="abs" role="img" aria-label="Surgeon and robotic arm in an operating theatre with holographic scan displays" style="inset:0;background:radial-gradient(ellipse at 70% 40%,rgba(120,170,220,.35),transparent 60%)"></div>
  <div class="brand" style="left:101px;top:18px"><span class="mark"></span>Quillamber</div>
  <nav class="nav">
    <a class="active" style="left:0">HOME</a>
    <a style="left:87px">SERVICES</a>
    <a style="left:199px">ABOUT</a>
    <a style="left:294px">BLOG</a>
    <a style="left:376px">CONTACT</a>
  </nav>
  <div class="btn" style="left:869px;top:24px;width:98px;height:35px">Log in <span class="dot"></span></div>
  <div class="btn btn-outline" style="left:974px;top:24px;width:118px;height:35px">Register <span class="dot"></span></div>
  <h1 class="abs hero-title">Guiding you to developing<br>the best medical software</h1>
  <div class="btn" style="left:97px;top:462px;width:199px;height:39px">Get our free guide <span class="dot"></span></div>
</header>

<section class="welcome">
  <div class="abs panel"></div>
  <div class="abs dots"></div>
  <div class="abs photo" role="img" aria-label="Software developers working at computers in a bright office"></div>
  <div class="abs eyebrow">
    <div class="small">Welcome to</div>
    <div class="big">Quillamber</div>
  </div>
  <p class="abs">Quillamber’ mission is to provide a custom software development service across a range of technologies by using best practice agile methodologies and tools to deliver customer value on time and within budget.</p>
  <div class="btn" style="left:623px;top:407px;width:157px;height:39px">Learn more <span class="dot"></span></div>
</section>

<section class="services">
  <h2 class="section-title" style="top:50px">Services We Provide</h2>
  <div class="card" style="left:100px">
    <svg width="94" height="92" viewBox="0 0 94 92" fill="none" stroke="#139fe0" stroke-width="2.5"><rect x="3" y="10" width="88" height="58" rx="3"/><path d="M3 58h88M40 68v12h14V68M30 82h34"/><rect x="12" y="18" width="16" height="32"/><rect x="36" y="22" width="20" height="24"/><rect x="62" y="30" width="20" height="16"/></svg>
    <h3>Web<br>Design</h3>
  </div>
  <div class="card" style="left:352px">
    <svg width="94" height="92" viewBox="0 0 94 92" fill="none" stroke="#139fe0" stroke-width="2.5"><rect x="14" y="50" width="66" height="40" rx="3"/><path d="M40 64l-6 6 6 6M54 64l6 6-6 6M49 62l-4 16"/><circle cx="47" cy="22" r="16"/><path d="M31 18h32"/></svg>
    <h3>Web<br>Development</h3>
  </div>
  <div class="card" style="left:605px">
    <svg width="94" height="92" viewBox="0 0 94 92" fill="none" stroke="#139fe0" stroke-width="2.5"><circle cx="22" cy="20" r="14"/><rect x="40" y="18" width="48" height="42" rx="3"/><path d="M48 30h32M48 40h32M48 50h22"/><path d="M8 88V62a14 14 0 0 1 28 0v26"/></svg>
    <h3>Application<br>Development</h3>
  </div>
  <div class="card" style="left:858px">
    <svg width="94" height="92" viewBox="0 0 94 92" fill="none" stroke="#139fe0" stroke-width="2.5"><rect x="6" y="6" width="82" height="76" rx="3"/><path d="M6 20h82M20 34l-6 5 6 5M30 34l6 5-6 5M44 39h34M16 54h62M16 64h48M16 74h30"/></svg>
    <h3>Custom Software<br>Development</h3>
  </div>
</section>

<section class="feature">
  <div class="abs" role="img" aria-label="Laboratory monitor showing cell and DNA imagery beside a microscope" style="left:560px;top:0;width:640px;height:561px;background:linear-gradient(90deg,rgba(255,255,255,0),rgba(220,235,245,.6))"></div>
  <h2 class="abs">Custom Software<br>Development</h2>
  <p class="abs">Using carefully selected software tools and carefully designed custom applications can make running your business so much more enjoyable. Quillamber can provide an upfront quote and regular progress updates on your project to give you piece of mind.</p>
  <div class="btn" style="left:105px;top:404px;width:157px;height:39px">Learn more <span class="dot"></span></div>
</section>

<section class="blog">
  <h2 class="section-title" style="top:80px">Our Latest Blog</h2>

  <article class="post" style="left:100px;top:168px;width:473px;height:488px">
    <div role="img" aria-label="Man using a tablet at a desk in a workshop office" style="height:281px;background:linear-gradient(135deg,#6e8aa0,#b8a58a 60%,#4d5c68)"></div>
    <div style="padding:22px 18px 0 19px">
      <div class="meta">10 April 2022 by editor</div>
      <h3 style="margin-top:4px">What makes a GREAT web application?</h3>
      <p style="margin-top:6px">So you’re looking to create a new web application. You’ll need to consider the budget, the requirements of your business and the functions you want the web application to perform for you.</p>
      <div class="more" style="margin-top:10px">LEARN MORE <span class="dot"></span></div>
    </div>
  </article>

  <article class="post" style="left:606px;top:168px;width:483px;height:225px">
    <div class="abs" role="img" aria-label="Hand pointing at a rising line chart" style="left:0;top:0;width:180px;height:225px;background:linear-gradient(135deg,#2c3946,#4b5966 60%,#a88a5a)"></div>
    <div class="abs" style="left:202px;top:32px;width:270px">
      <div class="meta">10 April 2022 by editor</div>
      <h3 style="margin-top:6px">The Absolutely Unbeatable Way Of Estimating...</h3>
      <p style="margin-top:6px;font-size:12.5px">Successful projects require accurate estimates of the effort required</p>
      <div class="more" style="margin-top:10px">LEARN MORE <span class="dot"></span></div>
    </div>
  </article>

  <article class="post" style="left:606px;top:428px;width:483px;height:225px">
    <div class="abs" role="img" aria-label="Hourglass held in a hand against a golden sunset" style="left:0;top:0;width:180px;height:225px;background:linear-gradient(135deg,#3a2a18,#c08a3e 55%,#5a3c1c)"></div>
    <div class="abs" style="left:202px;top:32px;width:270px">
      <div class="meta">1 July 2020 by editor</div>
      <h3 style="margin-top:6px">Making the most of your time investment</h3>
      <p style="margin-top:6px;font-size:12.5px">1. First Generation – Classic Time<br>&nbsp;Management Classic</p>
      <div class="more" style="margin-top:10px">LEARN MORE <span class="dot"></span></div>
    </div>
  </article>

  <div class="abs to-top">
    <svg width="50" height="50" viewBox="0 0 50 50" fill="none" stroke="#139fe0" stroke-width="1.5"><path d="M17 29l8-8 8 8"/></svg>
  </div>
</section>

<section class="signup">
  <h2 class="abs">Sign up for Clearpath Insights</h2>
  <div class="abs sub">At vero eos et accusamus et iusto odio dignissimos ducimus</div>
  <div class="abs field">Enter email address</div>
  <div class="abs submit">SUBMIT</div>
</section>

<footer class="footer">
  <div class="brand" style="left:100px;top:100px"><span class="mark"></span>Quillamber</div>
  <p class="abs about">Quillamber was founded in 1998. We have helped many customers achieve their dreams.</p>

  <h4 style="left:449px">Quick Links</h4>
  <div class="list" style="left:449px">Home<br>Services<br>About<br>Contact<br>Blog</div>

  <h4 style="left:627px">Contact Info</h4>
  <div class="contact-row" style="top:128px;left:632px">
    <svg width="16" height="22" viewBox="0 0 16 22"><path d="M8 1a7 7 0 0 0-7 7c0 5 7 13 7 13s7-8 7-13a7 7 0 0 0-7-7z" fill="#fff"/><circle cx="8" cy="8" r="2.6" fill="#0e1013"/></svg>
    <span>18 Harbour View Road<br>Meadowbrook Queensland 4207<br>Australia</span>
  </div>
  <div class="contact-row" style="top:214px">
    <svg width="18" height="18" viewBox="0 0 18 18"><path d="M4 1l3 4-2 2a10 10 0 0 0 6 6l2-2 4 3-2 3C8 17 1 10 1 4z" fill="none" stroke="#fff" stroke-width="1.6"/></svg>
    <span>Phone: +61 400 555 123</span>
  </div>
  <div class="contact-row" style="top:252px">
    <svg width="18" height="14" viewBox="0 0 18 14"><rect x="1" y="1" width="16" height="12" fill="#fff"/><path d="M1 1l8 7 8-7" fill="none" stroke="#0e1013" stroke-width="1.4"/></svg>
    <span>Email: hello@quillamber.com</span>
  </div>

  <h4 style="left:949px">Find Us Online</h4>
  <span class="social" style="left:949px"></span>
  <span class="social" style="left:988px"></span>
  <span class="social" style="left:1027px"></span>
  <span class="social" style="left:1066px"></span>

  <div class="abs rule"></div>
  <div class="abs legal" style="left:100px">©Copyright ©2022 quillamber. All Rights Reserved.</div>
  <div class="abs legal" style="left:890px;width:208px;text-align:right">Privacy Policy | Terms of Service</div>
</footer>

</body>
</html>
```